Marlow Fern Beauty Co.- Label template for Australian Small Batch Skincare company

Marlow Fern is a small batch, locally made, hand crafted beauty company which makes natural, ethically sourced beauty products for socially conscious consumers.
I need someone to design a product label template that have certain fields empty for example; ingredients, instructions, batch # and product name. I want to be able to fill these fields in later because I make a lot of products, and need flexibility. I want this as a template so I can fill in these fields before sending to printer.
I need two different label sizes;
-60ml amber jar. Internal Dimensions 5.5cm including lid x 50mm round diameter.
-30ml amber jar. Internal dimensions 5cm including lid x 40mm round diameter
Colour of Label: Either rose gold or white font. Depending on what looks the best. On Black background.
Target Market(s)
I am a professional working woman, wife and mother. I use products that are work for me and contain pure ingredients. I try to live a healthy lifestyle and I like products that support this.Financially secure women. Professionals. Might have own business. Majority are full time workers. $80k plus. Urban dwellers. Clean living supporters. Use organics. Have healthy diets. Mothers whose children are 10 years +.
Industry/Entity Type
Skin Care Product
Font styles to use
Other font styles liked:
- Typo (typewriter look font)
Requirements
Must have
- product label template that have certain fields empty for example; ingredients, instructions, batch # and product name. I want to be able to fill these fields in later because I make a lot of products, and need flexibility. I want this as a template so I can fill in these fields before sending to printer.
- Logo
- Ingredients- Blank field
- Space for Product name- Blank field
- Space for Product description – Blank field
- Space for Instructions- Blank field.
- Batch number (and a blank field for filling out later)
- 60 or 30 ml
- Tagline – nurturing kind hearts, fierce minds, & brave spirits
- Hand crafted with love in Melbourne
- Website- www.marlowfernbeautycompany.example
- Black background, Rose gold font. Typo font. (Font that looks like typewriter)
Nice to have
- Art Deco design elements. Rose gold on black background. I want this label to represent my artisan approach to skin care formulation and production. Everything is handmade by me.
Should not have
- Mass production feel

```html
<!DOCTYPE html>
<html lang="en">
<head>
<meta charset="utf-8">
<title>Marlow Fern Beauty Co. – Label Template</title>
<link href="https://fonts.googleapis.com/css2?family=Special+Elite&display=swap" rel="stylesheet">
<style>
  :root {
    --sheet: #ffffff;
    --sheet-edge: #c9a088;
    --label-black: #1c1b1b;
    --logo-panel: #2b2727;
    --rose-gold: #c9a088;
    --rose-gold-soft: #a8806b;
    --ink-white: #f4f1ee;
  }
  * { box-sizing: border-box; margin: 0; padding: 0; }
  html, body { width: 1200px; height: 875px; overflow: hidden; background: var(--sheet); }
  body { font-family: "Special Elite", "Courier New", monospace; }

  .sheet {
    position: relative; width: 1200px; height: 875px;
    border: 1px solid var(--sheet-edge); background: var(--sheet);
  }
  .label {
    position: absolute; left: 35px; width: 1128px; height: 398px;
    background: var(--label-black); color: var(--rose-gold);
  }
  .label--framed { top: 28px; }
  .label--plain { top: 449px; }
  .label > * { position: absolute; }

  .label-frame { left: 0; top: 0; width: 1128px; height: 398px; }
  .corner-ornament {
    width: 30px; height: 30px;
    background: radial-gradient(circle, var(--rose-gold) 0%, var(--rose-gold-soft) 45%, transparent 72%);
  }
  .corner-ornament--tl { left: 6px; top: 8px; }
  .corner-ornament--tr { right: 6px; top: 8px; }
  .corner-ornament--bl { left: 6px; bottom: 8px; }
  .corner-ornament--br { right: 6px; bottom: 8px; }

  /* Information column */
  .info-column { left: 37px; top: 48px; width: 300px; }
  .field-heading {
    display: flex; align-items: center; gap: 8px;
    color: var(--ink-white); font-size: 13.5px; line-height: 18px;
  }
  .field-rule { width: 115px; height: 10px; }
  .field-body { color: var(--rose-gold); font-size: 12.6px; line-height: 18.3px; margin-bottom: 8px; }
  .field-heading--batch { margin-top: 2px; }

  /* Centre column */
  .brand-panel {
    left: 428px; top: 28px; width: 273px; height: 135px;
    background: var(--logo-panel);
    display: flex; align-items: center; justify-content: center; text-align: center;
  }
  .brand-name { color: var(--rose-gold); font-size: 26px; line-height: 32px; }
  .divider { left: 455px; width: 218px; height: 12px; }
  .product-name { left: 428px; width: 273px; text-align: center; font-size: 22px; color: var(--rose-gold); }
  .product-description {
    left: 440px; width: 250px; text-align: center;
    color: var(--ink-white); font-size: 12.8px; line-height: 17.5px;
  }
  .swirl {
    width: 92px; height: 44px;
    background: radial-gradient(ellipse at center, var(--rose-gold-soft) 0%, rgba(168,128,107,0.35) 45%, transparent 75%);
  }
  .swirl--left { left: 342px; }
  .swirl--right { left: 688px; }
  .volume { left: 428px; width: 273px; text-align: center; font-size: 16px; color: var(--rose-gold); }

  /* Right column */
  .tagline-frame { left: 826px; top: 62px; width: 248px; height: 147px; }
  .tagline {
    left: 826px; top: 78px; width: 248px; text-align: center;
    color: var(--ink-white); font-size: 14.5px; line-height: 21px;
  }
  .origin {
    left: 826px; top: 225px; width: 248px; text-align: center;
    color: var(--rose-gold); font-size: 14.5px; line-height: 21px;
  }
  .floral-ornament {
    left: 890px; top: 283px; width: 122px; height: 30px;
    background: radial-gradient(ellipse at center, var(--rose-gold) 0%, var(--rose-gold-soft) 35%, transparent 72%);
  }
  .website {
    left: 790px; top: 334px; width: 320px; text-align: center;
    color: var(--ink-white); font-size: 13.2px; letter-spacing: -0.2px;
  }
</style>
</head>
<body>
<main class="sheet">

  <!-- Framed label -->
  <section class="label label--framed" aria-label="60ml label with frame">
    <svg class="label-frame" viewBox="0 0 1128 398" aria-hidden="true">
      <g fill="var(--rose-gold)">
        <rect x="50" y="9" width="1030" height="12"/>
        <rect x="50" y="376" width="1030" height="12"/>
        <rect x="9" y="54" width="11" height="290"/>
        <rect x="1108" y="54" width="11" height="290"/>
      </g>
      <path d="M60 28 L1068 28 L1100 58 L1100 340 L1068 370 L60 370 L28 340 L28 58 Z"
            fill="none" stroke="var(--rose-gold)" stroke-width="1.6"/>
    </svg>
    <div class="corner-ornament corner-ornament--tl" role="img" aria-label="Corner flourish ornament"></div>
    <div class="corner-ornament corner-ornament--tr" role="img" aria-label="Corner flourish ornament"></div>
    <div class="corner-ornament corner-ornament--bl" role="img" aria-label="Corner flourish ornament"></div>
    <div class="corner-ornament corner-ornament--br" role="img" aria-label="Corner flourish ornament"></div>

    <div class="info-column">
      <p class="field-heading">Ingredients:
        <svg class="field-rule" viewBox="0 0 115 10" aria-hidden="true"><line x1="2" y1="5" x2="113" y2="5" stroke="var(--rose-gold)"/><circle cx="2" cy="5" r="1.6" fill="var(--rose-gold)"/><circle cx="113" cy="5" r="1.6" fill="var(--rose-gold)"/><path d="M57 1 L61 5 L57 9 L53 5 Z" fill="var(--rose-gold)"/></svg>
      </p>
      <p class="field-body">Lorem ipsum dolor sit amet, consectetur adipiscing elit, sed do eiusmod tempor incididunt ut labore et dolore magna aliqua. Ut enim ad minim veniam, quis nostrud exercitation ullamco laboris</p>
      <p class="field-heading">Instructions:
        <svg class="field-rule" viewBox="0 0 115 10" aria-hidden="true"><line x1="2" y1="5" x2="113" y2="5" stroke="var(--rose-gold)"/><circle cx="2" cy="5" r="1.6" fill="var(--rose-gold)"/><circle cx="113" cy="5" r="1.6" fill="var(--rose-gold)"/><path d="M57 1 L61 5 L57 9 L53 5 Z" fill="var(--rose-gold)"/></svg>
      </p>
      <p class="field-body">Duis aute irure dolor in reprehenderit in voluptate velit esse cillum dolore eu fugiat nulla pariatur. Excepteur sint occaecat cupidatat non proident, sunt in culpa qui officia deserunt mollit anim id est laborum</p>
      <p class="field-heading field-heading--batch">Batch #:&nbsp;&nbsp;
        <svg class="field-rule" viewBox="0 0 115 10" aria-hidden="true"><line x1="2" y1="5" x2="113" y2="5" stroke="var(--rose-gold)"/><circle cx="2" cy="5" r="1.6" fill="var(--rose-gold)"/><circle cx="113" cy="5" r="1.6" fill="var(--rose-gold)"/><path d="M57 1 L61 5 L57 9 L53 5 Z" fill="var(--rose-gold)"/></svg>
      </p>
    </div>

    <div class="brand-panel"><p class="brand-name">Marlow Fern<br>Beauty Co.</p></div>
    <svg class="divider" style="top:192px" viewBox="0 0 218 12" aria-hidden="true"><line x1="0" y1="6" x2="218" y2="6" stroke="var(--rose-gold)" stroke-width="1.4"/><path d="M109 0 L114 6 L109 12 L104 6 Z" fill="var(--label-black)" stroke="var(--rose-gold)"/></svg>
    <p class="product-name" style="top:220px">Product Name</p>
    <svg class="divider" style="top:268px" viewBox="0 0 218 12" aria-hidden="true"><line x1="0" y1="6" x2="218" y2="6" stroke="var(--rose-gold)" stroke-width="1.4"/><path d="M109 0 L114 6 L109 12 L104 6 Z" fill="var(--label-black)" stroke="var(--rose-gold)"/></svg>
    <div class="swirl swirl--left" style="top:283px" role="img" aria-label="Scroll flourish ornament"></div>
    <p class="product-description" style="top:282px">Product description Product description Product description</p>
    <div class="swirl swirl--right" style="top:283px" role="img" aria-label="Scroll flourish ornament"></div>
    <svg class="divider" style="top:323px" viewBox="0 0 218 12" aria-hidden="true"><line x1="0" y1="6" x2="218" y2="6" stroke="var(--rose-gold)" stroke-width="1.4"/></svg>
    <p class="volume" style="top:342px">60ml</p>

    <svg class="tagline-frame" viewBox="0 0 248 147" aria-hidden="true">
      <path d="M30 6 Q124 -6 218 6 Q222 28 244 38 L244 109 Q222 119 218 141 Q124 153 30 141 Q26 119 4 109 L4 38 Q26 28 30 6 Z" fill="none" stroke="var(--rose-gold)" stroke-width="1.6"/>
      <path d="M35 12 Q124 2 213 12 Q218 31 238 42 L238 105 Q218 116 213 135 Q124 145 35 135 Q30 116 10 105 L10 42 Q30 31 35 12 Z" fill="none" stroke="var(--rose-gold)" stroke-width="1.2"/>
    </svg>
    <p class="tagline">nurturing<br>kind hearts,<br>fierce minds,<br>&amp; brave spirits</p>
    <p class="origin">Hand crafted with love<br>in Melbourne</p>
    <div class="floral-ornament" role="img" aria-label="Floral scroll ornament"></div>
    <p class="website">www.marlowfernbeautycompany.example</p>
  </section>

  <!-- Plain label -->
  <section class="label label--plain" aria-label="60ml label without frame">
    <div class="info-column">
      <p class="field-heading">Ingredients:
        <svg class="field-rule" viewBox="0 0 115 10" aria-hidden="true"><line x1="2" y1="5" x2="113" y2="5" stroke="var(--rose-gold)"/><circle cx="2" cy="5" r="1.6" fill="var(--rose-gold)"/><circle cx="113" cy="5" r="1.6" fill="var(--rose-gold)"/><path d="M57 1 L61 5 L57 9 L53 5 Z" fill="var(--rose-gold)"/></svg>
      </p>
      <p class="field-body">Lorem ipsum dolor sit amet, consectetur adipiscing elit, sed do eiusmod tempor incididunt ut labore et dolore magna aliqua. Ut enim ad minim veniam, quis nostrud exercitation ullamco laboris</p>
      <p class="field-heading">Instructions:
        <svg class="field-rule" viewBox="0 0 115 10" aria-hidden="true"><line x1="2" y1="5" x2="113" y2="5" stroke="var(--rose-gold)"/><circle cx="2" cy="5" r="1.6" fill="var(--rose-gold)"/><circle cx="113" cy="5" r="1.6" fill="var(--rose-gold)"/><path d="M57 1 L61 5 L57 9 L53 5 Z" fill="var(--rose-gold)"/></svg>
      </p>
      <p class="field-body">Duis aute irure dolor in reprehenderit in voluptate velit esse cillum dolore eu fugiat nulla pariatur. Excepteur sint occaecat cupidatat non proident, sunt in culpa qui officia deserunt mollit anim id est laborum</p>
      <p class="field-heading field-heading--batch">Batch #:&nbsp;&nbsp;
        <svg class="field-rule" viewBox="0 0 115 10" aria-hidden="true"><line x1="2" y1="5" x2="113" y2="5" stroke="var(--rose-gold)"/><circle cx="2" cy="5" r="1.6" fill="var(--rose-gold)"/><circle cx="113" cy="5" r="1.6" fill="var(--rose-gold)"/><path d="M57 1 L61 5 L57 9 L53 5 Z" fill="var(--rose-gold)"/></svg>
      </p>
    </div>

    <div class="brand-panel"><p class="brand-name">Marlow Fern<br>Beauty Co.</p></div>
    <svg class="divider" style="top:194px" viewBox="0 0 218 12" aria-hidden="true"><line x1="0" y1="6" x2="218" y2="6" stroke="var(--rose-gold)" stroke-width="1.4"/></svg>
    <p class="product-name" style="top:222px">Product Name</p>
    <svg class="divider" style="top:262px" viewBox="0 0 218 12" aria-hidden="true"><line x1="0" y1="6" x2="218" y2="6" stroke="var(--rose-gold)" stroke-width="1.4"/><path d="M109 0 L114 6 L109 12 L104 6 Z" fill="var(--label-black)" stroke="var(--rose-gold)"/></svg>
    <div class="swirl swirl--left" style="top:280px" role="img" aria-label="Scroll flourish ornament"></div>
    <p class="product-description" style="top:278px">Product description Product description Product description</p>
    <div class="swirl swirl--right" style="top:280px" role="img" aria-label="Scroll flourish ornament"></div>
    <svg class="divider" style="top:316px" viewBox="0 0 218 12" aria-hidden="true"><line x1="0" y1="6" x2="218" y2="6" stroke="var(--rose-gold)" stroke-width="1.4"/></svg>
    <p class="volume" style="top:336px">60ml</p>

    <svg class="tagline-frame" viewBox="0 0 248 147" aria-hidden="true">
      <path d="M30 6 Q124 -6 218 6 Q222 28 244 38 L244 109 Q222 119 218 141 Q124 153 30 141 Q26 119 4 109 L4 38 Q26 28 30 6 Z" fill="none" stroke="var(--rose-gold)" stroke-width="1.6"/>
      <path d="M35 12 Q124 2 213 12 Q218 31 238 42 L238 105 Q218 116 213 135 Q124 145 35 135 Q30 116 10 105 L10 42 Q30 31 35 12 Z" fill="none" stroke="var(--rose-gold)" stroke-width="1.2"/>
    </svg>
    <p class="tagline">nurturing<br>kind hearts,<br>fierce minds,<br>&amp; brave spirits</p>
    <p class="origin">Hand crafted with love<br>in Melbourne</p>
    <div class="floral-ornament" role="img" aria-label="Floral scroll ornament"></div>
    <p class="website">www.marlowfernbeautycompany.example</p>
  </section>

</main>
</body>
</html>
```